Business Cards for an 'affordable luxury' inner city home builder in Calgary.

We need a business card design that emulates the progressive, innovative, culture of our company and the modern style of our homes. Use our website www.velmarcrest-ab.com as a reference for the product we build.

Our company builds homes in the inner city space of Calgary, Alberta. We build affordable luxury.

Target Market(s)

Young professional Families

Contact Information for Business Card

Try to maintain consistency with the logo font and the card font.

Requirements
Must have
• The details must include: Name, education, title, phone number, website and email (Address is not as important)
• The design must be uniques (like our logo), elegant, sophisticated and modern.

```html
<!DOCTYPE html>
<html lang="en">
<head>
<meta charset="utf-8">
<title>Velmar Crest Homes Ltd – Business Card</title>
<link rel="stylesheet" href="https://fonts.googleapis.com/css2?family=Questrial&family=Open+Sans:wght@400&family=EB+Garamond:wght@400&family=Libre+Caslon+Text:wght@400&display=swap">
<style>
  :root {
    --page-bg: #ffffff;
    --card-front: #aaa7c3;
    --card-back: #bab8cd;
    --swoosh: #f2f2f2;
    --ink: #333333;
    --ink-dark: #111111;
    --rule: #222222;
    --frame-dark: #4a4a4e;
    --frame-mid: #9a9a9e;
    --frame-light: #e6e6ea;
  }
  html, body {
    margin: 0;
    padding: 0;
    width: 1200px;
    height: 1200px;
    overflow: hidden;
    background: var(--page-bg);
  }
  .canvas {
    position: relative;
    width: 1200px;
    height: 1200px;
  }
  .card {
    position: absolute;
    overflow: hidden;
  }
  .card--front { left: 139px; top: 92px; width: 927px; height: 529px; background: var(--card-front); }
  .card--back  { left: 137px; top: 651px; width: 939px; height: 529px; background: var(--card-back); }
  .card__art {
    position: absolute;
    inset: 0;
    width: 100%;
    height: 100%;
  }
  .brand {
    position: absolute;
    left: 186px;
    top: 45px;
    font-family: "Questrial", sans-serif;
    font-size: 31px;
    line-height: 39px;
    letter-spacing: 1.5px;
    color: var(--ink);
    text-transform: uppercase;
  }
  .brand__mark {
    position: absolute;
    left: 76px;
    top: 92px;
    width: 22px;
    height: 22px;
    background: var(--ink);
  }
  .web {
    position: absolute;
    font-family: "EB Garamond", serif;
    color: var(--ink-dark);
    white-space: nowrap;
    transform-origin: left bottom;
    transform: scaleX(0.78);
  }
  .web__label { margin-right: 0.7em; }
  .web--front { left: 525px; top: 44px; font-size: 31px; }
  .web--back  { left: 707px; top: 488px; font-size: 19px; }
  .contact {
    position: absolute;
    left: 33px;
    font-family: "Open Sans", sans-serif;
    font-size: 25px;
    color: var(--ink-dark);
    white-space: nowrap;
  }
  .contact--tel   { top: 389px; }
  .contact--email { top: 456px; }
  .fields {
    position: absolute;
    left: 91px;
    top: 183px;
    margin: 0;
    padding: 0;
    list-style: none;
    font-family: "Libre Caslon Text", serif;
    font-size: 23px;
    letter-spacing: 2px;
    color: var(--ink-dark);
  }
  .fields__row {
    position: relative;
    height: 34.5px;
    width: 505px;
  }
  .fields__line {
    position: absolute;
    left: 213px;
    right: 0;
    bottom: 8px;
    height: 1px;
    background: var(--rule);
  }
</style>
</head>
<body>
<div class="canvas">

  <section class="card card--front" aria-label="Card front">
    <svg class="card__art" viewBox="0 0 927 529" aria-hidden="true">
      <defs>
        <linearGradient id="frameFront" x1="0" y1="0" x2="1" y2="0">
          <stop offset="0" stop-color="#58575e"/>
          <stop offset="0.3" stop-color="#a4a3a8"/>
          <stop offset="0.45" stop-color="#76757c"/>
          <stop offset="0.68" stop-color="#e8e8ee"/>
          <stop offset="1" stop-color="#3f3f42"/>
        </linearGradient>
      </defs>
      <ellipse class="swoosh" cx="927" cy="264" rx="340" ry="268" fill="var(--swoosh)"/>
      <rect x="15" y="17" width="898" height="500" rx="7" fill="none" stroke="url(#frameFront)" stroke-width="9"/>
    </svg>
    <span class="brand__mark" aria-hidden="true"></span>
    <div class="brand">Velmar<br>Crest<br>Homes&nbsp;&nbsp;Ltd</div>
    <div class="web web--front"><span class="web__label">WEB:</span>www.velmarcrest-ab.com</div>
    <div class="contact contact--tel">Tel: 403-555-0148</div>
    <div class="contact contact--email">Email: projects@velmarcrest-ab.com</div>
  </section>

  <section class="card card--back" aria-label="Card back">
    <svg class="card__art" viewBox="0 0 939 529" aria-hidden="true">
      <defs>
        <linearGradient id="frameBack" x1="0" y1="0" x2="1" y2="0">
          <stop offset="0" stop-color="#58575e"/>
          <stop offset="0.3" stop-color="#a4a3a8"/>
          <stop offset="0.45" stop-color="#76757c"/>
          <stop offset="0.68" stop-color="#e8e8ee"/>
          <stop offset="1" stop-color="#2f2f33"/>
        </linearGradient>
      </defs>
      <rect x="17" y="17" width="909" height="498" rx="7" fill="none" stroke="url(#frameBack)" stroke-width="9"/>
    </svg>
    <ul class="fields">
      <li class="fields__row">Name:<span class="fields__line"></span></li>
      <li class="fields__row">Education:<span class="fields__line"></span></li>
      <li class="fields__row">Cell:<span class="fields__line"></span></li>
      <li class="fields__row">email<span class="fields__line"></span></li>
    </ul>
    <div class="web web--back"><span class="web__label">WEB:</span>www.velmarcrest-ab.com</div>
  </section>

</div>
</body>
</html>
```